Real Estate Marketing Postcards need a fresh look, Front & Back

I have a current postcard design (attached) that lacks design quality and too much use of color. I do like the basic color scheme, but I'm open to anything that cleans up the look and incorporates space for the existing text. I'm not opposed to a design with a white background, more white space. The design should be full bleed according to the attached specs. I would like this to be sent over in an Adobe format, something like InDesign.

The company logo will remain the same colors and appearance. The headshot will likely be updated in the coming weeks.

I am attaching a sample of a recent card plus a template from the printer showing the back of the card and location of the address and postage section that must remain blank. I am also including the logo and another logo designed for use with a white (or non blue) background.

(feel free to swap in stock photos of whatever house you want, but the front of the card should incorporate at least one photo of a house.)

Target Market(s)

Home owners.

Industry/Entity Type

Real Estate

Font styles to use
Sans Serif

Colors

Designer to choose colors to be used in the design.

Requirements
Must have
• Company logo, the headshot, the contact info on the back, a photo or photos of a house along with the text "Just Sold" or "Sold" featured on the front of the card.

```html
<!DOCTYPE html>
<html lang="en">
<head>
<meta charset="utf-8">
<title>Just Sold Postcard – Front &amp; Back</title>
<link rel="stylesheet" href="https://fonts.googleapis.com/css2?family=Montserrat:wght@500;600;700&family=Open+Sans:wght@400;600&display=swap">
<style>
  :root {
    --navy-dark: #1a2454;
    --navy: #26336c;
    --navy-light: #33448a;
    --lime: #b5d334;
    --ink: #1c1c24;
    --white: #ffffff;
    --mailing-grey: #e9e9ea;
    --page: #f2f2f0;
    --sky-dot: #8fc4ea;
  }
  * { box-sizing: border-box; margin: 0; padding: 0; }
  html, body { width: 1200px; height: 510px; overflow: hidden; background: var(--page); }
  .canvas { position: relative; width: 1200px; height: 510px; }

  .postcard {
    position: absolute; top: 73px; width: 518px; height: 365px; overflow: hidden;
    box-shadow: 0 4px 14px rgba(0,0,0,.18);
  }
  .postcard--front { left: 80px; background: linear-gradient(100deg, var(--navy-dark), var(--navy) 55%, var(--navy-light)); }
  .postcard--back { left: 624px; background: var(--white); }

  .front-art, .back-art { position: absolute; inset: 0; }

  .headline {
    position: absolute; font-family: "Montserrat", sans-serif; font-weight: 600;
    color: var(--lime); letter-spacing: 3px; line-height: 1; white-space: nowrap;
  }
  .headline--sold { right: 24px; top: 18px; font-size: 40px; }
  .headline--selling { left: 0; right: 0; top: 30px; text-align: center; font-size: 32px; }

  .brand-line {
    position: absolute; right: 30px; top: 314px; text-align: right;
    font-family: "Montserrat", sans-serif; white-space: nowrap;
  }
  .brand-line__name { color: var(--white); font-weight: 600; font-size: 21px; letter-spacing: 1.5px; line-height: 1; }
  .brand-line__tagline { color: var(--lime); font-weight: 500; font-size: 12.5px; margin-top: 5px; }
  .brand-line__rule { position: absolute; left: 494px; top: 312px; width: 3px; height: 38px; background: var(--lime); }

  .pitch {
    position: absolute; left: 0; right: 0; top: 110px; text-align: center;
    font-family: "Open Sans", sans-serif; font-size: 12.3px; letter-spacing: .9px;
    line-height: 1.3; color: var(--ink);
  }

  .headshot-frame {
    position: absolute; left: 21px; top: 153px; width: 105px; height: 104px;
    border: 4px solid var(--navy); background: var(--white); padding: 6px;
  }
  .headshot { width: 100%; height: 100%; background: linear-gradient(160deg, #7d7f8c, #b6b0ad 60%, #d7d9e0); }

  .agency-name {
    position: absolute; left: 146px; top: 196px;
    display: flex; align-items: center; gap: 7px; white-space: nowrap;
    font-family: "Open Sans", sans-serif; font-weight: 600; font-size: 14px;
    color: var(--navy); line-height: 1;
  }
  .agency-name__dot { width: 12px; height: 12px; border-radius: 50%; background: var(--sky-dot); flex: none; }

  .contact {
    position: absolute; left: 362px; top: 168px; white-space: nowrap;
    font-family: "Open Sans", sans-serif; font-size: 10.6px; letter-spacing: .8px;
    line-height: 12.2px; color: var(--ink); list-style: none;
  }
  .contact-rule { position: absolute; left: 126px; top: 253px; width: 368px; height: 3px; background: var(--navy); }
  .mailing-area { position: absolute; left: 0; right: 0; top: 258px; bottom: 0; background: var(--mailing-grey); }
</style>
</head>
<body>
<main class="canvas">

  <section class="postcard postcard--front" aria-label="Postcard front">
    <svg class="front-art" width="518" height="365" viewBox="0 0 518 365">
      <defs>
        <linearGradient id="house-photo-tone" x1="0" y1="0" x2="0" y2="1">
          <stop offset="0" stop-color="#8d93b3"/>
          <stop offset=".35" stop-color="#c9a7b2"/>
          <stop offset=".6" stop-color="#6f7688"/>
          <stop offset="1" stop-color="#3c4150"/>
        </linearGradient>
      </defs>
      <path class="accent-bar" d="M0 60 H185 C200 60 200 66 215 66 H0 Z" fill="var(--lime)"/>
      <path class="accent-rule" d="M185 61 H492" stroke="var(--lime)" stroke-width="1" fill="none"/>
      <path class="house-photo" role="img" aria-label="Photo of a two-storey suburban house with lit windows at dusk"
            d="M0 84 H220 C240 84 240 72 262 72 H518 V280 H360 C340 280 340 298 318 298 H0 Z"
            fill="url(#house-photo-tone)"/>
    </svg>
    <h1 class="headline headline--sold">JUST SOLD!</h1>
    <div class="brand-line">
      <p class="brand-line__name">THE HILLSIDE REALTOR</p>
      <p class="brand-line__tagline">You Know It Won't Last Long!</p>
    </div>
    <span class="brand-line__rule"></span>
  </section>

  <section class="postcard postcard--back" aria-label="Postcard back">
    <svg class="back-art" width="518" height="365" viewBox="0 0 518 365">
      <defs>
        <linearGradient id="band-tone" x1="0" y1="0" x2="1" y2="0">
          <stop offset="0" stop-color="var(--navy-dark)"/>
          <stop offset="1" stop-color="var(--navy-light)"/>
        </linearGradient>
      </defs>
      <path class="header-band" d="M0 0 H518 V77 H100 C78 77 78 95 56 95 H0 Z" fill="url(#band-tone)"/>
    </svg>
    <h2 class="headline headline--selling">SELLING?</h2>
    <p class="pitch">There is no other agent who knows the Hillside market better.<br>Contact me today to get your home SOLD.</p>

    <div class="headshot-frame">
      <div class="headshot" role="img" aria-label="Agent headshot"></div>
    </div>
    <p class="agency-name"><span class="agency-name__dot"></span>Willow Brook Real Estate</p>
    <ul class="contact">
      <li>Marco Bellini</li>
      <li>“The Hillside Realtor</li>
      <li>Willow Brook Real Estate</li>
      <li>(301) 555-0142 Office</li>
      <li>(301) 555-0187 Cell</li>
      <li>www.hillsidehomes.net</li>
    </ul>
    <span class="contact-rule"></span>
    <div class="mailing-area"></div>
  </section>

</main>
</body>
</html>
```